Cozy Critters Hamster Food, Label Redo

To re do our current label and make it look professional and appealing to the customer

Label is 6 x 4 inch

Logo must stay same colour

Attached pic "Back" shows the pouch it will be used on

Target Market(s)

Customers buying hamster food

Industry/Entity Type

Pet Food

Requirements
Must have
• The same purple logo

```html
<!DOCTYPE html>
<html lang="en">
<head>
<meta charset="utf-8">
<title>Cozy Critters Hamster Mixture Label</title>
<link rel="stylesheet" href="https://fonts.googleapis.com/css2?family=Fredoka:wght@500;700&family=Dancing+Script:wght@700&family=Nunito+Sans:wght@400;700;800&display=swap">
<style>
  :root {
    --brand-purple: #7a4a9e;
    --deep-purple: #5a2f80;
    --text-purple: #6b3f92;
    --panel-lilac: #ece7f3;
    --box-lilac: #d9cfe8;
    --side-teal: #b5dcd8;
    --photo-warm: #d9a06a;
    --photo-cool: #9fcfcc;
    --white: #ffffff;
    --ink: #3b2a4d;
  }
  * { margin: 0; padding: 0; box-sizing: border-box; }
  html, body { width: 800px; height: 1200px; overflow: hidden; background: var(--white); }
  .label {
    position: relative; width: 800px; height: 1200px;
    background: var(--panel-lilac);
    font-family: "Nunito Sans", Arial, sans-serif; color: var(--text-purple);
    overflow: hidden;
  }
  .brand-block {
    position: absolute; left: 0; top: 0; width: 500px; height: 240px;
    background: var(--brand-purple);
    display: flex; align-items: center; justify-content: center; gap: 22px;
  }
  .brand-dot { width: 34px; height: 34px; border-radius: 50%; background: var(--white); }
  .brand-name {
    font-family: "Fredoka", Arial, sans-serif; font-weight: 700;
    font-size: 66px; color: var(--white); letter-spacing: 1px; text-transform: uppercase;
  }
  .side-column {
    position: absolute; left: 520px; top: 0; width: 280px; height: 1200px;
    background: var(--side-teal);
  }
  .product-title {
    position: absolute; left: 534px; top: 26px; width: 252px; height: 160px;
    background: var(--white); border: 5px solid var(--brand-purple);
    text-align: center; padding-top: 16px;
  }
  .product-title .tier {
    font-family: "Dancing Script", cursive; font-size: 52px; color: var(--brand-purple); line-height: 1;
  }
  .product-title .kind {
    font-family: "Fredoka", Arial, sans-serif; font-weight: 700; font-size: 31px;
    color: var(--deep-purple); line-height: 1.05; margin-top: 10px; letter-spacing: 0.5px;
  }
  .product-photo {
    position: absolute; left: 520px; top: 200px; width: 280px; height: 520px;
    background: radial-gradient(ellipse at 50% 45%, var(--photo-warm) 0%, #e8c39a 40%, var(--photo-cool) 80%);
  }
  .servings {
    position: absolute; left: 520px; top: 726px; width: 280px; height: 58px;
    background: var(--brand-purple); color: var(--white);
    font-family: "Fredoka", Arial, sans-serif; font-weight: 700; font-size: 38px;
    display: flex; align-items: center; justify-content: center; gap: 12px;
  }
  .servings .count { font-size: 46px; }
  .origin {
    position: absolute; left: 536px; top: 800px; width: 250px;
    display: flex; align-items: center; gap: 12px;
  }
  .origin .flag { width: 58px; height: 40px; background: linear-gradient(135deg, #2a3f8f 0%, #c8102e 50%, #2a3f8f 100%); }
  .origin .made {
    font-family: "Fredoka", Arial, sans-serif; font-weight: 700; font-size: 30px;
    color: var(--deep-purple); line-height: 1;
  }
  .product-codes {
    position: absolute; left: 536px; top: 885px;
    font-weight: 800; font-size: 21px; color: var(--deep-purple); line-height: 1.4;
  }
  .intro {
    position: absolute; left: 26px; top: 262px; width: 466px;
    font-size: 19.5px; line-height: 1.3; color: var(--text-purple);
  }
  .intro p + p { margin-top: 22px; }
  .details-box {
    position: absolute; left: 26px; top: 605px; width: 466px; height: 432px;
    background: var(--box-lilac); padding: 16px 18px;
    font-size: 15.5px; line-height: 1.3; color: var(--ink);
  }
  .details-box h3 { font-weight: 800; font-size: 16.5px; color: var(--deep-purple); }
  .details-box section + section { margin-top: 14px; }
  .grid { display: grid; grid-template-columns: 1fr 1fr; column-gap: 16px; }
  .contact {
    position: absolute; left: 26px; top: 1060px; width: 470px;
    color: var(--deep-purple);
  }
  .contact .email { font-weight: 800; font-size: 19px; }
  .contact .address { font-size: 16px; line-height: 1.3; margin-top: 14px; }
</style>
</head>
<body>
<div class="label">
  <header class="brand-block">
    <span class="brand-dot"></span>
    <span class="brand-name">Cozy Critters</span>
  </header>

  <aside class="side-column"></aside>
  <div class="product-title">
    <div class="tier">Premium</div>
    <div class="kind">HAMSTER<br>MIXTURE</div>
  </div>
  <div class="product-photo" role="img" aria-label="Photo of a golden hamster standing upright on a teal background"></div>
  <div class="servings"><span class="count">50</span><span>SERVINGS</span></div>
  <div class="origin">
    <div class="flag" role="img" aria-label="Union flag"></div>
    <div class="made">MADE IN<br>BRITAIN</div>
  </div>
  <div class="product-codes">
    <div>SKU: HP31</div>
    <div>EXPIRY: 01/01/2025</div>
  </div>

  <div class="intro">
    <p>Our Cozy Critters Hamster mixture has everything your pet needs! A mixture for hamsters with a high amount of crispy kibbles and a small amount of pellets. With amongst others pea flakes, wheat and oat flakes, peanuts and shrimps</p>
    <p>A hamster needs 10 to 20 grams of food daily, dwarfhamsters needs about 6 grams of food daily, depending on their life stage and health status. Make sure the animals eat all ingredients. Always give unlimited access to fresh water. Store in a cool and dark place.</p>
  </div>

  <div class="details-box">
    <section>
      <h3>Composition:</h3>
      <p>Derivatives of vegetable origin, cereals (6,5% wheat and oat flakes), vegetables (9% pea flakes), seeds, nuts (1,8% peanuts), minerals, oils and fats, crustaceans and molluscs (0,5% shrimps)</p>
    </section>
    <section>
      <h3>Additives:</h3>
      <div class="grid">
        <span>Vitamin A 10900 IU</span><span>E1 Iorn 0.2mg</span>
        <span>E6 Zinc 5.2mg</span><span>Vitamin D3 1450 IU</span>
        <span>Vitamin E 60 mg</span><span>Vitamin C 50 mg</span>
      </div>
    </section>
    <section>
      <h3>Analysis:</h3>
      <div class="grid">
        <span>Crude protein 15,07%</span><span>Crude fat 5,14%</span>
        <span>Crude fibre 7,82%</span><span>Crude ash 3,79%</span>
        <span>Calcium 5,33 g/kg</span><span>Phosphorus 0,72 g/kg</span>
        <span>Sodium 0,08 g/kg</span><span>Magnesium 0,02 g/kg</span>
      </div>
    </section>
  </div>

  <footer class="contact">
    <div class="email">Contact: sales@bramblesupply.co.uk</div>
    <div class="address">Bramble Supply Co, 4 Orchard Works, Kiln Road,<br>Alderbury, SP5 3AB</div>
  </footer>
</div>
</body>
</html>
```